Discreet simple classy for adult entertainment

I would like a matte black business card with gold writing for my business. Keeping it simple. Having my following:

Lana frost
Events. Entertainment. Promotions
0491726580

or alternatively could have what i had on my previous card below but i think i prefer the above as again - discretion.

Maybe a nice gold line thru the card or some other very simple design . Or not open to ideas/ can be doublesided if any good ideas with that.

included pics of my old bus card. not sure weather i want a photo on it or not. if i do it wont be the same pic. i kinda wanted a card that was discreet so if it was in someones wallet they wouldn't neccessarily realise it was from a stripper.

Target Market(s)

men

Industry/Entity Type

Business

Contact Information for Business Card

Lana frost
0491726580

Requirements
Nice to have
• i don't know i am really open to anything. im giving my cards to guys so something they can have in their wallet that is discreet preferably.

```html
<!DOCTYPE html>
<html lang="en">
<head>
<meta charset="utf-8">
<title>Lana Frost – Business Card</title>
<link rel="stylesheet" href="https://fonts.googleapis.com/css2?family=Pinyon+Script&family=Roboto:ital,wght@0,300;1,300&display=swap">
<style>
  :root {
    --card-black: #000000;
    --figure-grey: #262626;
    --name-band: rgba(255, 255, 255, 0.2);
    --edge-olive: #6a5e00;
    --text-white: #ffffff;
    --text-olive: #8a7c04;
  }
  html, body {
    margin: 0;
    padding: 0;
    width: 750px;
    height: 1200px;
    overflow: hidden;
    background: var(--card-black);
  }
  .card {
    position: relative;
    width: 750px;
    height: 1200px;
    background: var(--card-black);
    overflow: hidden;
  }
  .figure-silhouette {
    position: absolute;
    left: 0;
    top: 0;
    width: 260px;
    height: 1200px;
    background: linear-gradient(180deg, var(--figure-grey) 0%, #1c1c1c 55%, #141414 100%);
  }
  .edge-stripe {
    position: absolute;
    right: 0;
    top: 0;
    width: 45px;
    height: 1200px;
    background: var(--edge-olive);
  }
  .name-band {
    position: absolute;
    left: 0;
    top: 318px;
    width: 705px;
    height: 270px;
    background: var(--name-band);
  }
  .name {
    position: absolute;
    margin: 0;
    font-family: "Pinyon Script", cursive;
    font-weight: 400;
    font-size: 124px;
    line-height: 1;
    color: var(--text-white);
  }
  .name-first { left: 95px; top: 318px; }
  .name-last  { left: 340px; top: 408px; }
  .phone {
    position: absolute;
    right: 80px;
    top: 740px;
    margin: 0;
    font-family: "Roboto", sans-serif;
    font-weight: 300;
    font-size: 52px;
    line-height: 1;
    color: var(--text-white);
  }
  .services {
    position: absolute;
    right: 75px;
    top: 893px;
    margin: 0;
    padding: 0;
    list-style: none;
    text-align: right;
    font-family: "Roboto", sans-serif;
    font-weight: 300;
    font-style: italic;
    font-size: 52px;
    line-height: 66px;
    color: var(--text-olive);
    white-space: nowrap;
  }
</style>
</head>
<body>
  <main class="card">
    <div class="figure-silhouette" role="img" aria-label="Dark silhouette of a posing woman running down the left side of the card"></div>
    <div class="edge-stripe"></div>
    <div class="name-band"></div>
    <h1 class="name name-first">Lana</h1>
    <p class="name name-last">Frost</p>
    <p class="phone">0491 726 580</p>
    <ul class="services">
      <li>strip shows</li>
      <li>poker dealer</li>
      <li>bikini barmaid</li>
      <li>professional party waitress</li>
    </ul>
  </main>
</body>
</html>
```